Mailer 001

https://www.filecrate.example/sh/x4k2pq7rtz19wmn/Lb3vQeNcRy
Orentation: Landscape
SIZE: 5 1/2' by 10 1/2'
COLORS: 32cd32, 13e613, 21f721, 00FE00, 00D800, 00B200, 009900

Re-Elect Dalton Pierce
Utah House of Representatives
Questions? Please call! (801) 555-0147

Text for side 1

Promises Made - Promises Kept
- Again I Promise to continue to advocate for limited government
- Again I Promise to advocate for educational choice
- Again I Promise to promote fiscal responsibility, transparency, and accountability.
- Again I Promise to take seriously my pledge to protect individual and economic liberty.

Text for side 2

Principled Conservative
I am committed to my oath to uphold the U.S. Constitution and Utah Constitution. As an attorney who has studied these documents, I understand the principles of federalism and of our republican form of government. I also understand that big government is a threat to our freedoms, even at the state and local levels. I have a record of sponsoring and supporting legislation that makes government more efficient and less burdensome.
- Dalton Pierce

Let’s finish what WE started
www.DaltonPierceHD42.example

Note: side 2 needs room for address lables as this will be a mailer sent out in the US post
, This is a mailer for a client of mine. It will be mailed out soon.
There is a filecrate link so you can look at some of the work done previously, the work done before was not done by a professional, but it will give you an idea of the branding style. Colors should match previous branding.

feel free to ask questions if needed.

Filecrate: https://www.filecrate.example/sh/x4k2pq7rtz19wmn/Lb3vQeNcRy
Orientation: Landscape
SIZE: 5 1/2' by 10 1/2'

Re-Elect Dalton Pierce

Text for side 1

Text for side 2

Principled Conservative
- Dalton Pierce

www.DaltonPierceHD42.example

If you are unable to get to the filecrate you and download a zip file.
https://docs.storevault.example/file/d/8ZqP2mWtR5xJ7LnYcK4bHsDvFgAe/edit?usp=sharing

Please note: we are looking for fresh and creative designs, not designs that look like the old flyers done by non-professionals.

Make the designs fresh and creative, I know that is an old a tired bit of instructions and ambiguous, so to clear that up a bit.....if the design look like I could have knocked I personally could have done, that is not what I want.  Do not just cut and paste images, use transparency, complementary colors and fading.  The design should be artistic.

bring your creativity and artistic nature.

```html
<!DOCTYPE html>
<html lang="en">
<head>
<meta charset="utf-8">
<title>Re-Elect Dalton Pierce – Mailer</title>
<link rel="stylesheet" href="https://fonts.googleapis.com/css2?family=Oswald:wght@500;700&family=Roboto+Condensed:wght@400;500&family=Open+Sans:wght@400;600&display=swap">
<style>
  :root {
    --stage: #6d6d6d;
    --stage-dark: #4a4a4a;
    --green-bright: #00fe00;
    --green-mid: #13e613;
    --green-base: #00d800;
    --green-deep: #00b200;
    --green-dark: #009900;
    --lime: #32cd32;
    --white: #ffffff;
    --ink: #1d2a12;
    --rule: #8a8a8a;
    --photo-shirt: #5f8fcf;
    --photo-tone: #c9a58e;
  }
  * { box-sizing: border-box; margin: 0; padding: 0; }
  html, body { width: 1200px; height: 1000px; overflow: hidden; }
  body {
    position: relative;
    background: radial-gradient(ellipse at 50% 40%, var(--stage) 0%, var(--stage-dark) 100%);
    font-family: "Roboto Condensed", "Arial Narrow", sans-serif;
  }

  /* ---------- shared card ---------- */
  .mailer-card {
    position: absolute;
    width: 665px;
    height: 348px;
    overflow: hidden;
    box-shadow: 0 6px 18px rgba(0,0,0,.35);
  }

  /* ---------- campaign name block ---------- */
  .name-panel {
    position: absolute;
    display: flex;
    flex-direction: column;
    justify-content: center;
    background: var(--lime);
    border: 1px solid rgba(255,255,255,.5);
    color: var(--white);
    overflow: hidden;
  }
  .name-panel__kicker {
    font-family: "Roboto Condensed", sans-serif;
    font-weight: 500;
    line-height: 1;
  }
  .name-panel__name {
    display: flex;
    align-items: center;
    font-family: "Oswald", sans-serif;
    font-weight: 700;
    text-transform: uppercase;
    line-height: 1.05;
    white-space: nowrap;
  }
  .name-panel__mark {
    background: var(--white);
    border-radius: 50%;
    flex: none;
  }
  .name-panel__office {
    font-family: "Roboto Condensed", sans-serif;
    font-weight: 400;
    line-height: 1;
    white-space: nowrap;
    text-align: right;
  }

  .capitol-fade {
    position: absolute;
    background: radial-gradient(ellipse at 50% 40%, rgba(0,90,0,.28) 0%, rgba(0,90,0,.12) 45%, rgba(0,90,0,0) 75%);
  }

  /* ---------- front side ---------- */
  .mailer-front {
    left: 127px; top: 20px;
    background: linear-gradient(160deg, var(--green-bright) 0%, var(--green-mid) 45%, var(--green-base) 75%, var(--green-deep) 100%);
  }
  .mailer-front .capitol-fade { left: 110px; top: 10px; width: 230px; height: 300px; }
  .candidate-photo {
    position: absolute;
    left: 0; top: 40px;
    width: 238px; height: 308px;
    background:
      radial-gradient(ellipse 26% 22% at 40% 22%, var(--photo-tone) 0%, var(--photo-tone) 70%, rgba(0,0,0,0) 100%),
      linear-gradient(180deg, rgba(0,0,0,0) 0%, rgba(0,0,0,0) 40%, var(--photo-shirt) 41%, #3f6fae 100%);
    border-radius: 40% 40% 0 0 / 18% 18% 0 0;
  }
  .mailer-front .name-panel { left: 494px; top: 20px; width: 151px; height: 72px; padding: 5px 8px; gap: 3px; }
  .mailer-front .name-panel__kicker { font-size: 11px; }
  .mailer-front .name-panel__name { font-size: 20px; gap: 5px; }
  .mailer-front .name-panel__mark { width: 9px; height: 9px; }
  .mailer-front .name-panel__office { font-size: 9.5px; }

  .headline {
    position: absolute;
    font-family: "Oswald", sans-serif;
    font-weight: 700;
    color: var(--white);
    font-size: 33px;
    letter-spacing: 2px;
    line-height: 1;
    text-shadow: 0 1px 2px rgba(0,80,0,.35);
  }
  .headline--made { left: 252px; top: 116px; }
  .headline--kept { left: 387px; top: 156px; }
  .promise-intro {
    position: absolute;
    left: 245px; top: 215px;
    color: var(--white);
    font-size: 20.5px;
    font-weight: 500;
  }
  .promise-list {
    position: absolute;
    left: 245px; top: 246px;
    list-style: none;
    color: var(--white);
    font-size: 14px;
    line-height: 19.5px;
  }

  /* ---------- back side ---------- */
  .mailer-back {
    left: 313px; top: 396px;
    background: var(--white);
  }
  .message-panel {
    position: absolute;
    left: 0; top: 0;
    width: 366px; height: 348px;
    background: linear-gradient(150deg, var(--green-bright) 0%, var(--green-mid) 50%, var(--green-base) 100%);
  }
  .message-panel .capitol-fade { left: 40px; top: 20px; width: 300px; height: 320px; }
  .statement {
    position: absolute;
    left: 35px; top: 38px;
    width: 297px;
    font-family: "Open Sans", sans-serif;
    color: var(--ink);
    font-size: 9.2px;
    letter-spacing: -0.05px;
    line-height: 19.5px;
    text-align: justify;
  }
  .statement__title { font-weight: 600; }
  .statement__sign { text-align: right; font-weight: 600; }
  .closing-band {
    position: absolute;
    left: 35px; top: 272px;
    width: 310px; height: 58px;
    background: var(--white);
  }
  .closing-band__slogan {
    position: absolute;
    left: 7px; top: 5px;
    font-family: "Oswald", sans-serif;
    font-weight: 500;
    font-size: 17px;
    color: var(--green-deep);
    line-height: 1.1;
  }
  .closing-band__url {
    position: absolute;
    left: 7px; top: 32px;
    font-family: "Roboto Condensed", sans-serif;
    font-size: 14.5px;
    color: var(--green-dark);
  }
  .closing-band .name-panel { left: 207px; top: 4px; width: 99px; height: 50px; padding: 3px 5px; gap: 2px; }
  .closing-band .name-panel__kicker { font-size: 8px; }
  .closing-band .name-panel__name { font-size: 12.5px; gap: 4px; }
  .closing-band .name-panel__mark { width: 6px; height: 6px; }
  .closing-band .name-panel__office { font-size: 6.5px; }
  .address-area { position: absolute; left: 366px; top: 0; width: 299px; height: 348px; }
  .address-area svg { display: block; }
</style>
</head>
<body>

<section class="mailer-card mailer-front" aria-label="Mailer front">
  <div class="capitol-fade" role="img" aria-label="Faint Utah State Capitol building"></div>
  <div class="candidate-photo" role="img" aria-label="Portrait of the candidate in blue shirt and tie, arms crossed"></div>
  <div class="name-panel">
    <p class="name-panel__kicker">Re-Elect</p>
    <p class="name-panel__name"><span class="name-panel__mark"></span>Dalton Pierce</p>
    <p class="name-panel__office">Utah House of Representatives</p>
  </div>
  <h1 class="headline headline--made">PROMISES MADE</h1>
  <h1 class="headline headline--kept">PROMISES KEPT</h1>
  <p class="promise-intro">Again I Promise to</p>
  <ul class="promise-list">
    <li>continue to advocate for limited government</li>
    <li>advocate for educational choice</li>
    <li>promote fiscal responsibility, transparency, and accountability.</li>
    <li>take seriously my pledge to protect individual and economic liberty.</li>
  </ul>
</section>

<section class="mailer-card mailer-back" aria-label="Mailer back">
  <div class="message-panel">
    <div class="capitol-fade" role="img" aria-label="Faint Utah State Capitol building"></div>
    <div class="statement">
      <p class="statement__title">Principled Conservative</p>
      <p>I am committed to my oath to uphold the U.S. Constitution and Utah Constitution. As an attorney who has studied these documents, I understand the principles of federalism and of our republican form of government. I also understand that big government is a threat to our freedoms, even at the state and local levels. I have a record of sponsoring and supporting legislation that makes government more efficient and less burdensome.</p>
      <p class="statement__sign">- Dalton Pierce</p>
    </div>
    <div class="closing-band">
      <p class="closing-band__slogan">Let’s Finish What We Started</p>
      <p class="closing-band__url">www.DaltonPierceHD42.example</p>
      <div class="name-panel">
        <p class="name-panel__kicker">Re-Elect</p>
        <p class="name-panel__name"><span class="name-panel__mark"></span>Dalton Pierce</p>
        <p class="name-panel__office">Utah House of Representatives</p>
      </div>
    </div>
  </div>
  <div class="address-area">
    <svg width="299" height="348" viewBox="0 0 299 348" aria-label="Stamp box and address lines">
      <rect x="163.5" y="31.5" width="85" height="82" fill="none" stroke="var(--rule)" stroke-width="1"/>
      <g stroke="var(--rule)" stroke-width="1">
        <line x1="31" y1="150.5" x2="249" y2="150.5"/>
        <line x1="31" y1="178.5" x2="249" y2="178.5"/>
        <line x1="31" y1="206.5" x2="249" y2="206.5"/>
        <line x1="31" y1="234.5" x2="249" y2="234.5"/>
        <line x1="31" y1="262.5" x2="249" y2="262.5"/>
        <line x1="31" y1="296.5" x2="249" y2="296.5"/>
      </g>
    </svg>
  </div>
</section>

</body>
</html>
```